Flyer Design

I need a flyer as Iam starting a business which cleans Leather couches,sofas,chairs for residential and businesses.
We clean the interiors of automobiles and marine craft, boats large and small.
We would like to be able to get across the message that we are affordable, personal and reliable.
The Gold coast is our market and within this area there is a large amount of holiday apartments and houses which do experience high traffic to their living and dinning areas.

Target Market(s)

Target market Home,Apartment,Marine and Auto Owners

Industry/Entity Type

Residential

Requirements
Must have
• The flyer must have Company name which is BRIGHT HIDE CARE MOBILE NUMBER
0471932054
EMAIL marvtolk@quellnet.com
Colours would like bright Gold or green or Red eith black lettering very modern font
Nice to have
• I would like to keep it as simple and clean looking.but eye catching
Should not have
• Dont want the flyer to look like a Real Estate flyer or a pizza advertisement.

```html
<!DOCTYPE html>
<html lang="en">
<head>
<meta charset="utf-8">
<title>Bright Hide Care Flyer</title>
<link href="https://fonts.googleapis.com/css2?family=Montserrat:wght@500;600;700&display=swap" rel="stylesheet">
<style>
  :root {
    --page-bg: #ececec;
    --leather-dark: #141414;
    --leather-mid: #2a2a2a;
    --stitch: #d8d8d8;
    --text-light: #ffffff;
    --gold: #e3b52c;
    --sofa-red: #c8321c;
    --chair-brown: #7a4a26;
    --seat-grey: #a9ab9c;
    --seat-white: #e6e3da;
  }
  * { margin: 0; padding: 0; box-sizing: border-box; }
  html, body { width: 1200px; height: 1000px; overflow: hidden; }
  body { background: var(--page-bg); font-family: "Montserrat", sans-serif; position: relative; }

  .flyer {
    position: absolute; left: 180px; top: 150px; width: 847px; height: 657px;
    background: radial-gradient(ellipse at 50% 45%, var(--leather-mid) 0%, var(--leather-dark) 75%);
    color: var(--text-light); overflow: hidden;
  }
  .stitch {
    position: absolute; left: 3px; right: 3px; height: 0;
    border-top: 2px dashed var(--stitch);
  }
  .stitch--t1 { top: 35px; }
  .stitch--t2 { top: 98px; }
  .stitch--b1 { top: 526px; }
  .stitch--b2 { top: 591px; }

  .brand-name {
    position: absolute; left: 0; right: 0; top: 42px; text-align: center;
    font-weight: 700; font-size: 46px; letter-spacing: 8px; line-height: 50px;
  }
  .service-copy {
    position: absolute; font-weight: 600; font-size: 15px; line-height: 28px;
    letter-spacing: 4px; text-transform: uppercase;
  }
  .service-copy--home { left: 85px; top: 137px; }
  .service-copy--vehicle { left: 333px; top: 385px; }

  .photo { position: absolute; border-radius: 10px; }
  .photo--sofa { left: 465px; top: 122px; width: 200px; height: 118px;
    background: linear-gradient(180deg, #e2503a, var(--sofa-red) 60%, #8a1f10); }
  .photo--armchair { left: 692px; top: 130px; width: 118px; height: 130px;
    background: linear-gradient(180deg, #9a6238, var(--chair-brown)); }
  .photo--seats { left: 97px; top: 342px; width: 201px; height: 148px;
    background: linear-gradient(90deg, var(--seat-grey) 0%, var(--seat-grey) 45%, var(--seat-white) 55%, var(--seat-white) 100%); }

  .tagline {
    position: absolute; left: 0; right: 0; top: 262px; text-align: center;
    font-weight: 700; font-size: 54px; line-height: 66px; letter-spacing: 1px;
    color: var(--gold); padding-left: 10px;
  }

  .call-label {
    position: absolute; left: 28px; top: 541px;
    font-weight: 700; font-size: 33px; letter-spacing: 3.5px; line-height: 38px;
  }
  .phone-number {
    position: absolute; left: 317px; top: 530px;
    font-weight: 700; font-size: 54px; letter-spacing: 12px; line-height: 58px;
  }
  .email {
    position: absolute; left: 0; right: 0; top: 611px; text-align: center;
    font-weight: 600; font-size: 17px; letter-spacing: 6px;
    text-transform: uppercase;
  }
</style>
</head>
<body>
  <main class="flyer">
    <div class="stitch stitch--t1"></div>
    <h1 class="brand-name">BRIGHT HIDE CARE</h1>
    <div class="stitch stitch--t2"></div>

    <p class="service-copy service-copy--home">Leather couches, sofas,<br>chairs for residential<br>and businesses.</p>
    <div class="photo photo--sofa" role="img" aria-label="Red leather two-seat sofa"></div>
    <div class="photo photo--armchair" role="img" aria-label="Brown leather armchair"></div>

    <h2 class="tagline">We Clean Leather</h2>

    <div class="photo photo--seats" role="img" aria-label="Grey car seat and white boat seat in leather"></div>
    <p class="service-copy service-copy--vehicle">The interiors of automobiles<br>and marine craft, boats large<br>and small.</p>

    <div class="stitch stitch--b1"></div>
    <p class="call-label">CALL NOW</p>
    <p class="phone-number">0471932054</p>
    <div class="stitch stitch--b2"></div>

    <p class="email">marvtolk@quellnet.com</p>
  </main>
</body>
</html>
```